Tervo's Glen

I need a Bussiness Card for my new company in Miami Beach, my company is based in Winwood Miami and all around me is arts soo I would like my card with stripes, art design.

Artists, Actress, actors, show bussiness

It Company

• Art Design

```html
<!DOCTYPE html>
<html lang="en">
<head>
<meta charset="utf-8">
<title>Tervo's Glen – Business Card</title>
<link href="https://fonts.googleapis.com/css2?family=Source+Sans+3:ital,wght@0,400;0,600;0,700;1,400&display=swap" rel="stylesheet">
<style>
  :root {
    --page-bg: #d9d6d2;
    --card-bg: #eef0f1;
    --ink: #4a3a3a;
    --name: #6b1e24;
    --accent: #b3202a;
    --maroon: #6a1a20;
    --brand-red: #9e1f26;
    --partner-navy: #1d3f86;
    --icon: #7a2a30;
  }
  * { margin: 0; padding: 0; box-sizing: border-box; }
  html, body {
    width: 1200px; height: 969px; overflow: hidden;
    background: var(--page-bg);
    font-family: "Source Sans 3", "Myriad Pro", sans-serif;
  }
  .card {
    position: absolute; left: 150px; top: 228px;
    width: 900px; height: 514px;
    background: var(--card-bg);
    box-shadow: 0 10px 30px rgba(0,0,0,0.18);
    overflow: hidden;
  }
  .contact { position: absolute; left: 57px; top: 82px; color: var(--ink); }
  .contact__name { font-size: 29px; font-weight: 600; color: var(--name); line-height: 1.1; }
  .contact__role { font-size: 23px; color: var(--accent); margin-top: 6px; line-height: 1.1; }
  .contact__email { font-size: 21px; font-style: italic; margin-top: 6px; line-height: 1.1; }
  .contact__lines { list-style: none; margin-top: 38px; }
  .contact__lines li {
    display: flex; align-items: center; gap: 14px;
    font-size: 21px; height: 36px;
  }
  .contact__lines svg { width: 18px; height: 22px; flex: none; }
  .contact__address { font-size: 21px; line-height: 34px; margin-top: 22px; }
  .contact__web { font-size: 21px; font-style: italic; color: var(--accent); letter-spacing: 1px; line-height: 34px; }

  .brand {
    position: absolute; left: 500px; top: 100px; width: 360px;
    display: flex; align-items: center; gap: 16px;
  }
  .brand__mark { width: 58px; height: 58px; border-radius: 50%; background: #e8a124; flex: none; }
  .brand__name { font-size: 60px; font-weight: 700; color: var(--brand-red); line-height: 1; }

  .partner {
    position: absolute; left: 520px; top: 290px; width: 340px;
    display: flex; align-items: center; gap: 16px;
  }
  .partner__mark { width: 62px; height: 62px; border-radius: 50%; background: #1c1c1c; flex: none; }
  .partner__name { font-size: 40px; font-weight: 700; color: var(--partner-navy); line-height: 1.02; }

  .stripe { position: absolute; left: 0; bottom: 0; width: 900px; height: 10px; }
</style>
</head>
<body>
  <main class="card">
    <section class="contact">
      <h1 class="contact__name">Dario Velasco</h1>
      <p class="contact__role">Tv Producer, Talent Hunt</p>
      <p class="contact__email">dariovelasco@tervosglen.net</p>
      <ul class="contact__lines">
        <li>
          <svg viewBox="0 0 18 22" aria-hidden="true"><rect x="2" y="1" width="14" height="20" rx="2" fill="none" stroke="var(--icon)" stroke-width="2.4"/><rect x="7" y="16" width="4" height="2" fill="var(--icon)"/></svg>
          555-204-7719
        </li>
        <li>
          <svg viewBox="0 0 18 22" aria-hidden="true"><rect x="0" y="2" width="18" height="18" rx="2" fill="var(--icon)"/></svg>
          @tervosglen
        </li>
        <li>
          <svg viewBox="0 0 18 22" aria-hidden="true"><rect x="0" y="2" width="18" height="18" rx="2" fill="var(--icon)"/></svg>
          @tervosglen
        </li>
      </ul>
      <p class="contact__address">418 Nw 31st St Miami<br>Florida 33199</p>
      <p class="contact__web">www.tervosglen.net</p>
    </section>

    <div class="brand">
      <span class="brand__mark"></span>
      <span class="brand__name">Tervo's Glen</span>
    </div>

    <div class="partner">
      <span class="partner__mark"></span>
      <span class="partner__name">Forge Works Productions</span>
    </div>

    <svg class="stripe" viewBox="0 0 900 10" preserveAspectRatio="none" aria-hidden="true">
      <polygon points="0,0 595,0 588,10 0,10" fill="var(--maroon)"/>
      <polygon points="603,0 900,0 900,10 596,10" fill="var(--accent)"/>
    </svg>
  </main>
</body>
</html>
```